Ledgerwise Business Card Design

Business Card Design for new business called Ledgerwise focused on selling business software to small and medium size companies who have outgrown Tallyhouse. Similar companies would be Tallyhouse, Vemo, BrightCore. Also Dealharbor would be good to look at for additional ideas around look and feel.

Target Market(s)

Business to Business

Industry/Entity Type

Information Technology

Contact Information for Business Card

Standard Business Card Information

Font styles to use
Sans Serif

```html
<!DOCTYPE html>
<html lang="en">
<head>
<meta charset="utf-8">
<title>Ledgerwise Business Card</title>
<link rel="stylesheet" href="https://fonts.googleapis.com/css2?family=Arimo:wght@400;700&display=swap">
<style>
  :root {
    --stage: #e9e6e1;
    --card-white: #ffffff;
    --card-shade: #e6e6e6;
    --brand-blue: #1f5a8a;
    --brand-blue-light: #3a78a8;
    --brand-orange: #f0831f;
    --brand-orange-dark: #c9661a;
    --text-dark: #333333;
    --text-grey: #555555;
  }
  * { margin: 0; padding: 0; box-sizing: border-box; }
  html, body { width: 1200px; height: 950px; overflow: hidden; }
  body {
    background: var(--stage);
    font-family: "Arimo", Arial, sans-serif;
    display: flex;
    flex-direction: column;
    align-items: center;
    justify-content: center;
    gap: 50px;
  }
  .card {
    position: relative;
    width: 700px;
    height: 400px;
    border-radius: 6px;
    overflow: hidden;
    box-shadow: 0 8px 24px rgba(0,0,0,0.18);
  }
  /* Front */
  .card-front { background: linear-gradient(160deg, var(--card-white) 55%, var(--card-shade)); }
  .card-front .swoosh { position: absolute; inset: 0; }
  .brand {
    position: absolute; left: 40px; top: 92px;
    display: flex; align-items: center; gap: 12px;
  }
  .brand-name {
    font-weight: 700; font-size: 40px; color: var(--brand-blue);
    letter-spacing: -0.5px;
  }
  .brand-dot {
    width: 30px; height: 30px; border-radius: 50%;
    background: var(--brand-orange);
  }
  .holder {
    position: absolute; right: 50px; top: 118px;
    text-align: right; color: #fff;
  }
  .holder-name { font-weight: 700; font-size: 22px; letter-spacing: 0.5px; }
  .holder-title { font-size: 17px; letter-spacing: 0.5px; margin-top: 2px; }
  .contacts {
    position: absolute; left: 40px; top: 178px;
    list-style: none; font-size: 19px; color: var(--text-dark);
  }
  .contacts li { display: flex; align-items: center; gap: 12px; height: 28px; }
  .contacts svg { width: 16px; height: 16px; fill: var(--brand-blue); flex: none; }
  .address {
    position: absolute; right: 70px; bottom: 48px;
    font-size: 19px; color: var(--text-grey); line-height: 1.4;
  }
  /* Back */
  .card-back {
    background: linear-gradient(120deg, var(--brand-orange) 40%, var(--brand-orange-dark));
    display: flex; flex-direction: column; align-items: center; justify-content: center; gap: 18px;
  }
  .back-brand { display: flex; align-items: center; gap: 14px; }
  .back-brand .brand-name { color: #fff; font-size: 46px; }
  .back-brand .brand-dot { background: #fff; width: 34px; height: 34px; }
  .back-web { color: rgba(255,255,255,0.85); font-size: 18px; letter-spacing: 2px; }
</style>
</head>
<body>
  <section class="card card-front">
    <svg class="swoosh" viewBox="0 0 700 400" preserveAspectRatio="none" aria-hidden="true">
      <defs>
        <linearGradient id="bandBlue" x1="0" y1="0" x2="1" y2="0">
          <stop offset="0" stop-color="#1f5a8a"/>
          <stop offset="1" stop-color="#3a78a8"/>
        </linearGradient>
      </defs>
      <path d="M0,40 C260,46 520,110 700,270 V0 H0 Z" fill="url(#bandBlue)"/>
      <path d="M0,40 C260,46 520,110 700,270" fill="none" stroke="#f0831f" stroke-width="7"/>
      <path d="M0,46 C260,52 515,118 700,280" fill="none" stroke="#ffffff" stroke-width="5"/>
    </svg>

    <div class="brand">
      <span class="brand-name">Ledgerwise</span>
      <span class="brand-dot"></span>
    </div>

    <div class="holder">
      <div class="holder-name">MAREN HOLT</div>
      <div class="holder-title">PRESIDENT</div>
    </div>

    <ul class="contacts">
      <li><svg viewBox="0 0 16 16"><path d="M3 1h3l1.5 4-2 1.2a8 8 0 0 0 4.3 4.3L11 8.5l4 1.5v3a2 2 0 0 1-2 2A12 12 0 0 1 1 3a2 2 0 0 1 2-2z"/></svg>555 0142 7781</li>
      <li><svg viewBox="0 0 16 16"><path d="M4 1h7v4H4zM1 6h14v7h-3v2H4v-2H1zM5 10v4h6v-4z"/></svg>555 0198 3364</li>
      <li><svg viewBox="0 0 16 16"><path d="M1 3h14v10H1zM2 4.2v.6l6 4 6-4v-.6z"/></svg>maren@ledgerwise.example</li>
      <li><svg viewBox="0 0 16 16"><path d="M8 1a7 7 0 1 0 0 14A7 7 0 0 0 8 1zm0 1.5c.8 0 1.8 1.8 2 4.5H6c.2-2.7 1.2-4.5 2-4.5zM6 9h4c-.2 2.7-1.2 4.5-2 4.5S6.2 11.7 6 9z"/></svg>www.ledgerwise.example</li>
    </ul>

    <address class="address" style="font-style: normal;">
      2710 Harlow Avenue<br>
      Cedar Glen, NY 10980
    </address>
  </section>

  <section class="card card-back">
    <div class="back-brand">
      <span class="brand-name">Ledgerwise</span>
      <span class="brand-dot"></span>
    </div>
    <div class="back-web">www.ledgerwise.example</div>
  </section>
</body>
</html>
```